Verdant Medispa Business Card

need a business card for our medispa, attached please see the logo.
our website is https://verdantmedispa-example.com

Sorina Belcourt, MD
Internal Medicine

555-204-7193

Sorina@verdantmedispa-example.com

Www.Verdantmedispa-example.com

738 E Harlow Blvd N, Ste 512, Katy, TX 77981

Target Market(s)

MedSpa, Cosmetics, Esthetics

Industry/Entity Type

MedicalSpa

Contact Information for Business Card

Please see the attached business card which i pulled from the internet. I like the idea back as a logo and front with info.

Font styles to use
Decorative

Requirements
Must have
• Color should be matching with Logo and Website theme, Also I like to have QR code for the website

```html
<!DOCTYPE html>
<html lang="en">
<head>
<meta charset="utf-8">
<title>Verdant Medispa – Business Card</title>
<link href="https://fonts.googleapis.com/css2?family=Raleway:wght@400;700&display=swap" rel="stylesheet">
<style>
  :root {
    --backdrop: #ded5d3;
    --card: #7b6754;
    --card-dark: #35271d;
    --ink-light: #ffffff;
    --ink-dark: #3a2a1f;
    --ink-soft: #d9c6b4;
    --qr-fill: #efe6dd;
  }
  html, body {
    margin: 0;
    padding: 0;
    width: 1200px;
    height: 1200px;
    overflow: hidden;
    background: var(--backdrop);
    font-family: "Raleway", sans-serif;
  }
  .card {
    position: absolute;
    left: 316px;
    width: 568px;
    height: 341px;
    background: var(--card);
    overflow: hidden;
  }
  .card--front { top: 217px; }
  .card--back  { top: 681px; }

  .front-shape {
    position: absolute;
    inset: 0;
    width: 100%;
    height: 100%;
  }
  .front-wordmark {
    position: absolute;
    left: 208px;
    top: 150px;
    width: 330px;
    text-align: center;
    color: var(--ink-light);
    font-weight: 400;
    font-size: 34px;
    letter-spacing: 1px;
    white-space: nowrap;
  }

  .holder-name {
    position: absolute;
    left: 56px;
    top: 52px;
    margin: 0;
    color: var(--ink-light);
    font-weight: 700;
    font-size: 27px;
  }
  .holder-title {
    position: absolute;
    left: 56px;
    top: 88px;
    margin: 0;
    color: var(--ink-dark);
    font-weight: 400;
    font-size: 20px;
  }
  .back-wordmark {
    position: absolute;
    left: 392px;
    top: 78px;
    width: 156px;
    text-align: center;
    color: var(--ink-soft);
    font-weight: 400;
    font-size: 18px;
    white-space: nowrap;
  }
  .website-qr {
    position: absolute;
    left: 440px;
    top: 112px;
    width: 60px;
    height: 60px;
    background: var(--qr-fill);
    border-radius: 3px;
  }

  .appointment {
    position: absolute;
    left: 56px;
    top: 221px;
    color: var(--ink-light);
    font-size: 15px;
    line-height: 21px;
  }
  .appointment-row { display: flex; align-items: baseline; }
  .appointment-line {
    display: inline-block;
    width: 118px;
    border-bottom: 1px dotted var(--ink-light);
    margin-left: 1px;
  }

  .contact {
    position: absolute;
    left: 236px;
    top: 200px;
    margin: 0;
    padding: 0;
    list-style: none;
    color: var(--ink-light);
    font-size: 15px;
    line-height: 21px;
  }
  .contact-item { display: flex; align-items: center; }
  .contact-icon {
    width: 14px;
    height: 14px;
    margin-right: 13px;
    fill: var(--ink-light);
    flex: none;
  }

  .address-band {
    position: absolute;
    left: 0;
    top: 278px;
    width: 100%;
    height: 29px;
    background: var(--card-dark);
    color: var(--ink-light);
    font-size: 16px;
    line-height: 29px;
    text-align: center;
  }
</style>
</head>
<body>

<section class="card card--front" aria-label="Card front">
  <svg class="front-shape" viewBox="0 0 915 550" preserveAspectRatio="none" aria-hidden="true">
    <path d="M0 0 H117 L372 462 Q418 548 540 550 H0 Z" fill="var(--card-dark)"/>
    <path d="M121 0 L376 462 Q424 548 548 550" fill="none" stroke="var(--ink-light)" stroke-width="5"/>
  </svg>
  <div class="front-wordmark">Verdant Medispa</div>
</section>

<section class="card card--back" aria-label="Card back">
  <h1 class="holder-name">Sorina Belcourt, MD</h1>
  <p class="holder-title">Internal Medicine</p>
  <div class="back-wordmark">Verdant Medispa</div>
  <div class="website-qr" role="img" aria-label="QR code linking to verdantmedispa-example.com"></div>

  <div class="appointment">
    <div class="appointment-row">date:<span class="appointment-line"></span></div>
    <div class="appointment-row">time:<span class="appointment-line"></span></div>
  </div>

  <ul class="contact">
    <li class="contact-item">
      <svg class="contact-icon" viewBox="0 0 24 24" aria-hidden="true"><path d="M6.6 10.8a15.1 15.1 0 0 0 6.6 6.6l2.2-2.2a1 1 0 0 1 1-.25 11.4 11.4 0 0 0 3.6.57 1 1 0 0 1 1 1V20a1 1 0 0 1-1 1A17 17 0 0 1 3 4a1 1 0 0 1 1-1h3.5a1 1 0 0 1 1 1c0 1.250.2 2.45.57 3.57a1 1 0 0 1-.25 1z"/></svg>
      555-204-7193
    </li>
    <li class="contact-item">
      <svg class="contact-icon" viewBox="0 0 24 24" aria-hidden="true"><path d="M2 5h20v14H2z M3.5 6.5l8.5 6.5 8.5-6.5" stroke="var(--card)" stroke-width="1.4"/></svg>
      sorina@verdantmedispa-example.com
    </li>
    <li class="contact-item">
      <svg class="contact-icon" viewBox="0 0 24 24" aria-hidden="true"><path d="M6 2v18l4.5-4.5 3 6.5 2.5-1.2-3-6.3H19z"/></svg>
      www.verdantmedispa-example.com
    </li>
  </ul>

  <div class="address-band">738 E Harlow Blvd N, Ste 512, Katy, TX 77981</div>
</section>

</body>
</html>
```